Mirela Dawn Business Card Design

I need a business card for my daughter. She has it all described in the file below. But it needs to be square in shape. http://www.mireladawn.example is her web site

Target Market(s)

18-35 year old women

Industry/Entity Type

Fashion

Contact Information for Business Card

Please look at the attached file as it has all the details.

Requirements
Must have
• Please look at the attached file as it has all the details.
Nice to have
Should not have

```html
<!DOCTYPE html>
<html lang="en">
<head>
<meta charset="utf-8">
<title>Mirela Dawn Business Card</title>
<link rel="stylesheet" href="https://fonts.googleapis.com/css2?family=Archivo+Narrow:wght@700&family=Kaushan+Script&family=Playfair+Display+SC:wght@400&family=Playfair+Display:wght@700&family=Work+Sans:wght@300;400&display=swap">
<style>
  :root {
    --backdrop-light: #e6e6e6;
    --backdrop-dark: #cbcbcb;
    --card-black: #0b0809;
    --name-pink: #d6a3cf;
    --tagline: #f4efec;
    --card-pink: #e8c4ba;
    --ink: #2a2324;
    --ink-soft: #4b4143;
    --dot: #6b5a5d;
  }
  * { box-sizing: border-box; margin: 0; padding: 0; }
  html, body { width: 1200px; height: 900px; overflow: hidden; }
  body {
    background: linear-gradient(120deg, var(--backdrop-light), var(--backdrop-dark));
    position: relative;
  }
  .card {
    position: absolute;
    top: 240px;
    width: 420px;
    height: 420px;
    box-shadow: 0 6px 18px rgba(0,0,0,0.18);
    overflow: hidden;
  }
  .card-front { left: 150px; background: var(--card-black); }
  .card-back { left: 630px; background: var(--card-pink); }

  .light-trails {
    position: absolute; inset: 0;
    background:
      radial-gradient(ellipse 40% 30% at 25% 35%, rgba(140,100,40,0.55), transparent 70%),
      radial-gradient(ellipse 35% 28% at 75% 65%, rgba(130,92,36,0.5), transparent 70%),
      radial-gradient(ellipse 20% 20% at 15% 80%, rgba(110,30,25,0.45), transparent 70%),
      radial-gradient(ellipse 30% 25% at 60% 20%, rgba(120,85,35,0.4), transparent 70%),
      var(--card-black);
  }
  .front-content {
    position: relative;
    height: 100%;
    display: flex; flex-direction: column; align-items: center; justify-content: center;
  }
  .brand-name {
    font-family: "Playfair Display SC", serif;
    font-weight: 400;
    font-size: 34px;
    letter-spacing: 5px;
    color: var(--name-pink);
    padding: 4px 14px;
    border-top: 2px solid var(--name-pink);
    border-bottom: 2px solid var(--name-pink);
    white-space: nowrap;
  }
  .tagline {
    margin-top: 16px;
    font-family: "Kaushan Script", cursive;
    font-size: 18px;
    letter-spacing: 1px;
    color: var(--tagline);
  }

  .back-content {
    height: 100%;
    padding: 0 24px;
    display: flex; flex-direction: column; align-items: center; justify-content: center;
    text-align: center;
    color: var(--ink);
  }
  .role {
    font-family: "Archivo Narrow", sans-serif;
    font-weight: 700;
    font-size: 22px;
    letter-spacing: 3.5px;
    text-transform: uppercase;
  }
  .niches {
    margin-top: 4px;
    font-family: "Work Sans", sans-serif;
    font-weight: 400;
    font-size: 12px;
    letter-spacing: 3px;
    color: var(--ink-soft);
  }
  .socials {
    list-style: none;
    margin-top: 28px;
    display: flex; flex-direction: column; align-items: center; gap: 8px;
    font-family: "Work Sans", sans-serif;
    font-weight: 300;
    font-size: 14px;
    letter-spacing: 1.5px;
    color: var(--ink-soft);
  }
  .socials li { display: flex; align-items: center; gap: 8px; white-space: nowrap; }
  .socials .marker {
    width: 9px; height: 9px; border-radius: 50%;
    background: var(--dot);
  }
  .links {
    margin-top: 30px;
    font-family: "Playfair Display", serif;
    font-weight: 700;
    font-size: 15px;
    letter-spacing: 1.5px;
    line-height: 1.45;
    white-space: nowrap;
  }
</style>
</head>
<body>
  <section class="card card-front">
    <div class="light-trails" role="img" aria-label="Dark long-exposure photograph of swirling gold and red light trails"></div>
    <div class="front-content">
      <h1 class="brand-name">MIRELA DAWN</h1>
      <p class="tagline">Let's talk fashion</p>
    </div>
  </section>

  <section class="card card-back">
    <div class="back-content">
      <h2 class="role">Blogger &amp; Vlogger</h2>
      <p class="niches">BEAUTY-FASHION-TRAVEL</p>
      <ul class="socials">
        <li><span class="marker"></span>pics.example/mireladawnxo</li>
        <li><span class="marker"></span>chirp.example/mireladawnxo</li>
        <li><span class="marker"></span>@mireladawnxo</li>
      </ul>
      <p class="links">Blog : mireladawn.example<br>Videos : videos.example/mireladawn</p>
    </div>
  </section>
</body>
</html>
```